Higher $ Now Guaranteed! Redesign Web Page(s) Style Composition and Color (Graphics design-not code)

We need a modern look for an existing website. You can either use or change the current logo. Choice of colors, fonts, style is up to you. Sample URLs and additional details are provided in the attached document. Most of our struggle has been the appearance of the directory listings (city) page.
----------------------------------------------------------------------------------
--> Increased Project Budget and Now Funds are GUARANTEED
--> Added an additional attachment in response to questions
-->THIS PROJECT IS FOR GRAPHICS/DESIGN NOT CODE
The project is mostly a few areas of text and colored boxes or lines. Hopefully a skilled designer can place these elements in an attractive layout and choose the right colors and styles. There are no complex drawings required for this project.

*** We are involved with other projects from time to time and expect that the winning designer will be given the first opportunity at this future work. ***

*** There is no requirement to do any code but if you submit a design feel free to indicate if you wish to be considered for any future code work on this site or others ***

Font styles to use
Sans Serif

Requirements
Must have
• Rounded corners on images and buttons with nice gradients or hover effects.
Nice to have
• Attached an additional descriptions document to help with these answers.
Should not have
• Small fonts, traditional older looking rectangular buttons, dull or boring color schemes

```html
<!DOCTYPE html>
<html lang="en">
<head>
<meta charset="utf-8">
<title>LedgerFinder.com – Tax Experts in Texas</title>
<link rel="stylesheet" href="https://fonts.googleapis.com/css2?family=Ubuntu:wght@400;500;700&display=swap">
<style>
:root{
  --ink:#2b2b2b;
  --muted:#555;
  --soft:#9a9a9a;
  --navy:#1f4150;
  --slate:#4a6f7f;
  --cyan:#0fb0cf;
  --sky:#4fbde5;
  --yellow:#fcc93b;
  --red:#e8505b;
  --green:#9fd46a;
  --green-text:#86c040;
  --link:#1f5f86;
  --tint:#faf9f3;
  --line:#e8e8e8;
  --bg:#f6f6f6;
}
*{box-sizing:border-box;margin:0;padding:0}
html,body{width:1051px;height:1200px;overflow:hidden}
body{position:relative;font-family:"Ubuntu",sans-serif;color:var(--ink);background:#fff}
.abs{position:absolute}
.page-bg{left:0;top:96px;width:1051px;height:982px;background:var(--bg)}

/* header */
.brand{left:64px;top:34px;display:flex;align-items:center;gap:8px;font-size:22px;font-weight:500;color:var(--slate)}
.brand .dot{width:14px;height:14px;border-radius:50%;background:var(--slate)}
.nav{left:532px;top:42px;display:flex;gap:42px;font-size:13px;color:#333;letter-spacing:.3px}
.phone{left:820px;top:32px;display:flex;align-items:center;gap:10px;color:var(--slate);font-size:20px;font-weight:500}

/* search */
.search{left:65px;top:96px;width:921px;height:64px;background:var(--cyan);border-radius:0 0 4px 4px;display:flex;align-items:center;padding-left:23px}
.search .label{color:#fff;font-weight:500;font-size:14px;width:135px}
.search .field{width:202px;height:33px;background:#fff;margin-right:16px;padding:9px 11px;color:#bbb;font-size:12px}
.search .btn{width:97px;height:33px;background:var(--yellow);border-radius:3px;color:#fff;font-weight:700;font-size:12px;display:flex;align-items:center;justify-content:center;gap:6px;box-shadow:0 2px 0 #e2ac1e}

/* listings */
.title{left:65px;top:182px;font-size:19px;font-weight:500;color:var(--navy)}
.listing{left:65px;width:527px;height:105px;background:#fff;border:1px solid var(--line)}
.listing .badges{position:absolute;left:0;top:0;width:157px;height:100%;background:var(--tint);border-right:1px solid var(--line)}
.badge{position:absolute;left:13px;display:flex;align-items:center;gap:7px;font-size:11.5px;color:#333}
.details{position:absolute;left:174px;top:9px;font-size:11px;line-height:17px}
.details .row{display:flex}
.details dt{width:64px;color:var(--muted)}
.details dd{color:#222}
.details a{color:var(--link);text-decoration:none}

/* pagination */
.pager{left:65px;top:1013px;display:flex;gap:2px}
.pager span{width:37px;height:34px;background:var(--cyan);color:#fff;font-size:11px;font-weight:500;display:flex;align-items:center;justify-content:center;box-shadow:0 2px 0 #0a8aa3}
.pager span:first-child{border-radius:3px 0 0 3px;width:38px}
.pager span:last-child{border-radius:0 3px 3px 0;width:41px}
.pager .active{background:var(--slate);box-shadow:0 2px 0 #3a5a68}
.results{left:474px;top:1023px;font-size:11px;color:#333}

/* sidebar */
.promo-art{left:676px;top:175px;width:250px;height:90px;border-radius:40px 40px 6px 6px;background:linear-gradient(180deg,#b07a55 0%,#f1d2bd 60%,#f6e2d5 100%)}
.promo{left:617px;top:260px;width:369px;height:268px;background:#fff;border:1px solid var(--line);border-radius:4px;text-align:center}
.promo h3{position:absolute;width:100%;font-size:14.5px;font-weight:500}
.promo p{position:absolute;width:100%;font-size:10.3px;color:var(--soft);line-height:14px}
.promo .cta{position:absolute;left:108px;width:152px;height:35px;border-radius:3px;color:#fff;font-weight:500;font-size:14px;letter-spacing:1.3px;display:flex;align-items:center;justify-content:center}
.cta.red{background:linear-gradient(#f0636d,var(--red));box-shadow:0 2px 0 #c43a44}
.cta.green{background:linear-gradient(#aedd7d,var(--green));box-shadow:0 2px 0 #7fb04b}
.promo hr{position:absolute;left:18px;width:331px;top:132px;border:0;border-top:2px solid #eee}

.experts{left:617px;top:539px;width:369px;height:373px;background:#fff;border:1px solid var(--line);border-radius:4px;overflow:hidden}
.experts header{height:43px;background:var(--sky);color:#fff;font-weight:500;font-size:14px;display:flex;align-items:center;justify-content:center;box-shadow:0 2px 0 #36a5cf}
.expert{position:absolute;left:17px;width:340px}
.expert .photo{position:absolute;left:0;top:0;width:114px;height:122px;border-radius:4px;background:linear-gradient(135deg,#7a6a55,#d9c6a8 55%,#5c4c3d)}
.expert .info{position:absolute;left:150px;top:2px;font-size:10.8px;line-height:17px;width:205px}
.expert .name{color:var(--navy)}
.expert .firm{color:var(--slate)}
.expert a{color:var(--slate);text-decoration:none}
.experts hr{position:absolute;left:17px;width:333px;top:201px;border:0;border-top:2px solid #eee}

/* footer */
.footer{left:0;top:1078px;width:1051px;height:122px;background:var(--navy)}
.fcol{top:1101px;font-size:10.3px;color:#fff;line-height:18.5px}
.fcol h4{font-size:11px;font-weight:500;letter-spacing:1px;color:#9fb2bb;margin-bottom:7px}
.flogo{left:857px;top:1122px;display:flex;align-items:center;gap:7px;color:#fff;font-size:20px;font-weight:500}
.flogo .dot{width:12px;height:12px;border-radius:50%;background:#fff}
</style>
</head>
<body>
<div class="abs page-bg"></div>

<header>
  <div class="abs brand"><span class="dot"></span>LedgerFinder.com</div>
  <nav class="abs nav"><span>HOME</span><span>GET LISTED</span><span>CONTACT US</span></nav>
  <div class="abs phone">
    <svg width="34" height="34" viewBox="0 0 34 34" fill="none" stroke="#4a6f7f" stroke-width="2.2" stroke-linecap="round">
      <path d="M8 6l5 0 2 7-3 2c2 4 5 7 9 9l2-3 7 2v5c0 2-2 3-4 3C14 30 4 20 4 10c0-2 2-4 4-4z"/>
      <path d="M20 3a11 11 0 0 1 11 11"/><path d="M20 8a6 6 0 0 1 6 6"/>
    </svg>
    555-014-2290
  </div>
</header>

<form class="abs search">
  <span class="label">FInd tax experts by</span>
  <div class="field">City</div>
  <div class="field">State</div>
  <div class="field">ZIP</div>
  <div class="btn">SEARCH
    <svg width="13" height="13" viewBox="0 0 13 13" fill="none" stroke="#fff" stroke-width="1.8"><circle cx="7.5" cy="5.5" r="4"/><path d="M4.5 8.5L1.5 11.5"/></svg>
  </div>
</form>

<h1 class="abs title">TAX EXPERTS IN TEXAS</h1>

<!-- listing template repeated -->
<article class="abs listing" style="top:217px">
  <div class="badges">
    <div class="badge" style="top:13px"><svg width="15" height="15"><circle cx="7.5" cy="7.5" r="7.5" fill="#7cc55a"/><path d="M4 7.8l2.4 2.4L11 5.5" stroke="#fff" stroke-width="1.8" fill="none"/></svg>Verified</div>
    <div class="badge" style="top:37px"><svg width="15" height="15"><rect x="1" y="6" width="3" height="8" fill="#f5b233"/><path d="M5 6l3-5c1.5 0 2 1 1.7 2.4L9 6h4c1 0 1.5 1 1.2 1.8l-1.6 5.2c-.3.7-.8 1-1.5 1H5z" fill="#f5b233"/></svg>Highly Recommended</div>
  </div>
  <dl class="details">
    <div class="row"><dt>Company</dt><dd>Levy Ledger</dd></div>
    <div class="row"><dt>Address</dt><dd>Maple Road 12A, Cedar Park Complex<br>Texas, USA. 75501</dd></div>
    <div class="row"><dt>Phone</dt><dd>555 010 4477</dd></div>
    <div class="row"><dt>Website</dt><dd><a>www.levyledger.com</a></dd></div>
  </dl>
</article>
<article class="abs listing" style="top:330px">
  <div class="badges">
    <div class="badge" style="top:13px"><svg width="15" height="15"><circle cx="7.5" cy="7.5" r="7.5" fill="#7cc55a"/><path d="M4 7.8l2.4 2.4L11 5.5" stroke="#fff" stroke-width="1.8" fill="none"/></svg>Verified</div>
    <div class="badge" style="top:37px"><svg width="15" height="15"><rect x="1" y="6" width="3" height="8" fill="#f5b233"/><path d="M5 6l3-5c1.5 0 2 1 1.7 2.4L9 6h4c1 0 1.5 1 1.2 1.8l-1.6 5.2c-.3.7-.8 1-1.5 1H5z" fill="#f5b233"/></svg>Highly Recommended</div>
  </div>
  <dl class="details">
    <div class="row"><dt>Company</dt><dd>Levy Ledger</dd></div>
    <div class="row"><dt>Address</dt><dd>Maple Road 12A, Cedar Park Complex<br>Texas, USA. 75501</dd></div>
    <div class="row"><dt>Phone</dt><dd>555 010 4477</dd></div>
    <div class="row"><dt>Website</dt><dd><a>www.levyledger.com</a></dd></div>
  </dl>
</article>
<article class="abs listing" style="top:443px">
  <div class="badges">
    <div class="badge" style="top:13px"><svg width="15" height="15"><circle cx="7.5" cy="7.5" r="7.5" fill="#7cc55a"/><path d="M4 7.8l2.4 2.4L11 5.5" stroke="#fff" stroke-width="1.8" fill="none"/></svg>Verified</div>
    <div class="badge" style="top:37px"><svg width="15" height="15"><rect x="1" y="6" width="3" height="8" fill="#f5b233"/><path d="M5 6l3-5c1.5 0 2 1 1.7 2.4L9 6h4c1 0 1.5 1 1.2 1.8l-1.6 5.2c-.3.7-.8 1-1.5 1H5z" fill="#f5b233"/></svg>Highly Recommended</div>
  </div>
  <dl class="details">
    <div class="row"><dt>Company</dt><dd>Levy Ledger</dd></div>
    <div class="row"><dt>Address</dt><dd>Maple Road 12A, Cedar Park Complex<br>Texas, USA. 75501</dd></div>
    <div class="row"><dt>Phone</dt><dd>555 010 4477</dd></div>
    <div class="row"><dt>Website</dt><dd><a>www.levyledger.com</a></dd></div>
  </dl>
</article>
<article class="abs listing" style="top:556px">
  <div class="badges">
    <div class="badge" style="top:13px"><svg width="15" height="15"><circle cx="7.5" cy="7.5" r="7.5" fill="#7cc55a"/><path d="M4 7.8l2.4 2.4L11 5.5" stroke="#fff" stroke-width="1.8" fill="none"/></svg>Verified</div>
    <div class="badge" style="top:37px"><svg width="15" height="15"><rect x="1" y="6" width="3" height="8" fill="#f5b233"/><path d="M5 6l3-5c1.5 0 2 1 1.7 2.4L9 6h4c1 0 1.5 1 1.2 1.8l-1.6 5.2c-.3.7-.8 1-1.5 1H5z" fill="#f5b233"/></svg>Highly Recommended</div>
  </div>
  <dl class="details">
    <div class="row"><dt>Company</dt><dd>Levy Ledger</dd></div>
    <div class="row"><dt>Address</dt><dd>Maple Road 12A, Cedar Park Complex<br>Texas, USA. 75501</dd></div>
    <div class="row"><dt>Phone</dt><dd>555 010 4477</dd></div>
    <div class="row"><dt>Website</dt><dd><a>www.levyledger.com</a></dd></div>
  </dl>
</article>
<article class="abs listing" style="top:669px">
  <div class="badges"></div>
  <dl class="details">
    <div class="row"><dt>Company</dt><dd>Levy Ledger</dd></div>
    <div class="row"><dt>Address</dt><dd>Maple Road 12A, Cedar Park Complex<br>Texas, USA. 75501</dd></div>
    <div class="row"><dt>Phone</dt><dd>555 010 4477</dd></div>
    <div class="row"><dt>Website</dt><dd><a>www.levyledger.com</a></dd></div>
  </dl>
</article>
<article class="abs listing" style="top:782px">
  <div class="badges"></div>
  <dl class="details">
    <div class="row"><dt>Company</dt><dd>Levy Ledger</dd></div>
    <div class="row"><dt>Address</dt><dd>Maple Road 12A, Cedar Park Complex<br>Texas, USA. 75501</dd></div>
    <div class="row"><dt>Phone</dt><dd>555 010 4477</dd></div>
    <div class="row"><dt>Website</dt><dd><a>www.levyledger.com</a></dd></div>
  </dl>
</article>
<article class="abs listing" style="top:895px">
  <div class="badges"></div>
  <dl class="details">
    <div class="row"><dt>Company</dt><dd>Levy Ledger</dd></div>
    <div class="row"><dt>Address</dt><dd>Maple Road 12A, Cedar Park Complex<br>Texas, USA. 75501</dd></div>
    <div class="row"><dt>Phone</dt><dd>555 010 4477</dd></div>
    <div class="row"><dt>Website</dt><dd><a>www.levyledger.com</a></dd></div>
  </dl>
</article>

<nav class="abs pager">
  <span><svg width="8" height="10"><path d="M6 1L2 5l4 4" stroke="#fff" stroke-width="2" fill="none"/></svg></span>
  <span>1</span><span class="active">2</span><span>3</span><span>4</span><span>5</span><span>6</span><span>7</span>
  <span><svg width="8" height="10"><path d="M2 1l4 4-4 4" stroke="#fff" stroke-width="2" fill="none"/></svg></span>
</nav>
<div class="abs results">show results 7 of 35 lists</div>

<aside>
  <div class="abs promo">
    <h3 style="top:26px;color:var(--red)">ARE YOU TAX PREPARER?</h3>
    <p style="top:48px">Our directories of tax professionals give you immediate access<br>to the very best tax preparers and income tax advisors in your area.</p>
    <div class="cta red" style="top:80px">SUBMIT LISTING</div>
    <hr>
    <h3 style="top:155px;color:var(--green-text)">HAVE A LOCAL TAX FIRM CONTACT ME</h3>
    <p style="top:177px">Our directories of tax professionals give you immediate access<br>to the very best tax preparers and income tax advisors in your area.</p>
    <div class="cta green" style="top:210px">GET STARTED</div>
  </div>
  <div class="abs promo-art" role="img" aria-label="Photo of a smiling woman leaning over the top of the card"></div>

  <section class="abs experts">
    <header>RELIABLE TAX EXPERTS</header>
    <div class="expert" style="top:61px">
      <div class="photo" role="img" aria-label="Portrait photo of a tax expert"></div>
      <div class="info"><div class="name">MARINA HOLT</div><div class="firm">Levy Ledger</div>Lorem ipsum dolor sit amet, consectetur adipiscing elit, sed do eiusmod tempor incididunt ut labore et dolore magna sed do eiusmod aliqua.<br><a>see more profile</a></div>
    </div>
    <hr>
    <div class="expert" style="top:223px">
      <div class="photo" role="img" aria-label="Portrait photo of a tax expert"></div>
      <div class="info"><div class="name">MARINA HOLT</div><div class="firm">Levy Ledger</div>Lorem ipsum dolor sit amet, consectetur adipiscing elit, sed do eiusmod tempor incididunt ut labore et dolore magna sed do eiusmod aliqua.<br><a>see more profile</a></div>
    </div>
  </section>
</aside>

<footer>
  <div class="abs footer"></div>
  <div class="abs fcol" style="left:65px"><h4>NAVIGATION</h4>Directory<br>Special Offers<br>Contact Us</div>
  <div class="abs fcol" style="left:222px"><h4>CONTACT</h4>PO Box 4410<br>Fairview, OR<br>97024</div>
  <div class="abs fcol" style="left:380px"><h4>LEGAL</h4>Pixel Harbor © 2015<br>website design<br>by brightnorthstudio.com</div>
  <div class="abs flogo"><span class="dot"></span>LedgerFinder.com</div>
</footer>
</body>
</html>
```